Trivanta Business Solutions

I need a business card design with logo for my business and management consultancy business. I am based in Singapore and I provide (i) accounting / bookkeeping services; (ii) management and business consultancy solutions; (iii) tax advisory and consultancy; and (iv) risk management and corporate governance. I want the design to be bold and outstanding yet doesn't give the impression that I take unnecessary risks.

Reason: To the designers who have gotten messages from me, I'm still waiting for some changes to be made.

Target Market(s)

Small to large enterprises which are willing to pay value for money and not necessarily the cheapest

Industry/Entity Type

Accounting

Contact Information for Business Card

Name, email address and mobile no.

Requirements
Must have
• If possible, could you incorporate the Sigma symbol as the E for Trivanta or the Equals sign to show that the business relates to finance / financials and that I provide solutions which may it easy for my clients.
Should not have
• Black / dark backgrounds

```html
<!DOCTYPE html>
<html lang="en">
<head>
<meta charset="utf-8">
<title>Trivanta Business Solutions – Business Card</title>
<link rel="stylesheet" href="https://fonts.googleapis.com/css2?family=Arimo:wght@400;700&family=Questrial&display=swap">
<style>
  :root {
    --backdrop: #b9babd;
    --card: #ffffff;
    --olive: #958a55;
    --olive-text: #8a7d3e;
    --ink: #2a2a2a;
    --rule: #9a9a9a;
    --band-text: #ffffff;
  }
  * { margin: 0; padding: 0; box-sizing: border-box; }
  html, body {
    width: 1200px;
    height: 800px;
    overflow: hidden;
    background: var(--backdrop);
  }
  .canvas {
    position: relative;
    width: 1200px;
    height: 800px;
  }
  .card {
    position: absolute;
    left: 400px;
    top: 50px;
    width: 400px;
    height: 700px;
    background: var(--card);
    box-shadow: 0 6px 18px rgba(0, 0, 0, 0.25);
    font-family: "Arimo", Arial, sans-serif;
  }
  .brand {
    position: absolute;
    left: 40px;
    top: 140px;
    display: flex;
    align-items: center;
    gap: 14px;
    color: var(--olive-text);
    font-weight: 700;
  }
  .brand-mark {
    width: 44px;
    height: 44px;
    background: var(--olive);
    flex: none;
  }
  .brand-name {
    display: flex;
    flex-direction: column;
    line-height: 1;
  }
  .brand-name .primary { font-size: 54px; letter-spacing: -1px; }
  .brand-name .secondary { font-size: 19px; margin-top: 4px; align-self: flex-end; }
  .holder {
    position: absolute;
    left: 40px;
    top: 298px;
  }
  .holder-name {
    font-family: "Questrial", Arial, sans-serif;
    font-size: 34px;
    color: var(--olive-text);
    letter-spacing: 1px;
    font-weight: 400;
  }
  .contact {
    list-style: none;
    margin-top: 14px;
    font-size: 17px;
    color: var(--ink);
    line-height: 1.35;
    letter-spacing: 0.3px;
  }
  .rule {
    position: absolute;
    left: 0;
    width: 100%;
    height: 1px;
    background: var(--rule);
  }
  .rule-top { top: 440px; }
  .rule-bottom { top: 646px; }
  .services {
    position: absolute;
    left: 0;
    top: 468px;
    width: 100%;
    height: 164px;
    background: var(--olive);
    list-style: none;
    padding: 28px 40px 0;
    color: var(--band-text);
    font-size: 15.5px;
    line-height: 1.75;
  }
</style>
</head>
<body>
<main class="canvas">
  <article class="card">
    <header class="brand">
      <span class="brand-mark" aria-hidden="true"></span>
      <span class="brand-name">
        <span class="primary">Trivanta</span>
        <span class="secondary">Business Solutions</span>
      </span>
    </header>

    <section class="holder">
      <h1 class="holder-name">LEAH TANAKA</h1>
      <ul class="contact">
        <li>M - 123 XXX XXXX</li>
        <li>E - leah@trivantasolutions.com</li>
      </ul>
    </section>

    <div class="rule rule-top"></div>
    <ul class="services">
      <li>- accounting / bookkeeping services</li>
      <li>- management and business consultancy solutions</li>
      <li>- tax advisory and consultancy</li>
      <li>- risk management and corporate governance</li>
    </ul>
    <div class="rule rule-bottom"></div>
  </article>
</main>
</body>
</html>
```